Halvorn Minerals Web Design

Require a Web page design for an international mining and private investment company currently based in Dubai, UAE. I would like to view designs that incorporate our current corporate logo design aimed at communicating global business development/expansion across a diversity of commodities within the mining and investment sectors.

We are a global organisation with global experience and strategy with specific business development focus in Africa, Central and South America.

Target Market(s)

Mining industry, finance, fund raising, brokering, private equity and public stock exchanges.

Industry/Entity Type

Mining

Number of Pages Required

5+ page

Font styles to use
Sans Serif

Colors

Designer to choose colors to be used in the design.

Requirements
Must have
• Corporate logo, description of who we are, what we do, corporate mission, vision & strategy.
Nice to have
• Inclusion of images, photos, interactive maps/graphics and video.

```html
<!DOCTYPE html>
<html lang="en">
<head>
<meta charset="utf-8">
<title>Halvorn Minerals</title>
<link href="https://fonts.googleapis.com/css2?family=Lato:wght@400;700;900&family=Open+Sans:wght@400;600&display=swap" rel="stylesheet">
<style>
:root{
  --gold:#b8913f;
  --ink:#1f1f1f;
  --text:#555;
  --grey-band:#e8e8e8;
  --footer:#161616;
  --white:#fff;
}
*{box-sizing:border-box;margin:0;padding:0}
html,body{width:1200px;height:3175px;overflow:hidden;background:var(--white)}
body{position:relative;font-family:"Open Sans",Arial,sans-serif;color:var(--text)}
.heading{font-family:"Lato",Arial,sans-serif;font-weight:900;color:var(--ink);text-transform:uppercase}
.btn{position:absolute;background:var(--gold);color:var(--white);font-family:"Lato",Arial,sans-serif;font-weight:700;font-size:16px;border-radius:24px;display:flex;align-items:center;justify-content:center;text-transform:uppercase}

/* header */
.site-header{position:absolute;left:0;top:0;width:1200px;height:93px;background:var(--white)}
.brand{position:absolute;left:98px;top:26px;display:flex;align-items:center;gap:12px}
.brand-mark{width:38px;height:38px;border-radius:50%;background:var(--gold)}
.brand-name{font-family:"Lato",Arial,sans-serif;font-weight:700;font-size:24px;color:var(--gold);text-transform:uppercase;letter-spacing:1px}
.topbar{position:absolute;right:98px;top:17px;font-family:"Lato",Arial,sans-serif;font-size:16px;color:var(--ink);display:flex;gap:12px;align-items:center}
.topbar svg{vertical-align:-2px;margin-right:6px}
.main-nav{position:absolute;right:98px;top:56px;display:flex;gap:22px;font-family:"Lato",Arial,sans-serif;font-weight:700;font-size:16px;color:var(--ink);align-items:center}
.main-nav .active{color:var(--gold)}

/* hero */
.hero{position:absolute;left:0;top:93px;width:1200px;height:537px;background:linear-gradient(180deg,#1c2433 0%,#2b3242 45%,#4a4038 75%,#6b5030 100%)}
.hero-title{position:absolute;left:0;width:1200px;top:130px;text-align:center;font-family:"Lato",Arial,sans-serif;font-weight:900;font-size:72px;color:var(--white)}
.hero-sub{position:absolute;left:0;width:1200px;top:222px;text-align:center;font-size:27px;line-height:38px;color:var(--white)}
.hero-btn{position:absolute;left:495px;top:337px;width:210px;height:54px;border:2px solid var(--white);border-radius:28px;color:var(--white);font-family:"Lato",Arial,sans-serif;font-weight:700;font-size:17px;display:flex;align-items:center;justify-content:center}
.dots{position:absolute;left:563px;top:478px;display:flex;gap:6px}
.dots span{width:13px;height:13px;border-radius:50%;border:2px solid var(--white)}
.dots span.on{background:var(--white)}

/* welcome */
.welcome-box{position:absolute;left:98px;top:700px;width:568px;height:405px;border:2px solid #cfcfcf}
.welcome-box h1{position:absolute;left:34px;top:30px;font-size:34px;line-height:47px}
.welcome-box p{position:absolute;left:34px;width:455px;font-size:13px;line-height:27px}
.video{position:absolute;left:620px;top:740px;width:482px;height:326px;background:linear-gradient(135deg,#8b7a66,#4a3f36 55%,#2e2723)}
.video svg{position:absolute;left:211px;top:133px}

/* what we do */
.services{position:absolute;left:0;top:1183px;width:1200px;height:500px;background:var(--grey-band)}
.section-title{position:absolute;left:0;width:1200px;text-align:center;font-size:34px}
.service{position:absolute;top:150px;width:220px;text-align:center}
.service svg{display:block;margin:0 auto}
.service h3{font-family:"Lato",Arial,sans-serif;font-weight:700;font-size:20px;color:var(--ink);margin-top:22px}
.service p{font-size:14px;line-height:23px;margin-top:14px;color:#666}

/* why */
.why-photo{position:absolute;left:0;top:1683px;width:602px;height:487px;background:linear-gradient(160deg,#6e5a45,#c9b79d 45%,#e6e2dc 70%,#8e6a42)}
.why h2{position:absolute;left:663px;top:1735px;font-size:34px}
.why ul{position:absolute;left:663px;top:1805px;width:440px;list-style:none}
.why li{position:relative;padding-left:24px;font-size:14px;line-height:25px;margin-bottom:25px}
.why li svg{position:absolute;left:0;top:5px}

/* blog */
.blog-card{position:absolute;top:2336px;width:324px}
.blog-img{width:324px;height:209px}
.blog-card h3{font-family:"Lato",Arial,sans-serif;font-weight:700;font-size:20px;color:var(--ink);margin-top:30px}
.meta{font-size:13px;color:var(--gold);margin-top:12px;display:flex;align-items:center;gap:6px}
.meta .sep{color:#999;margin:0 4px}
.blog-card p{font-size:13px;line-height:24px;margin-top:14px}
.read-more{font-family:"Lato",Arial,sans-serif;font-weight:700;font-size:14px;color:var(--gold);margin-top:14px;text-transform:uppercase}

/* footer */
.site-footer{position:absolute;left:0;top:2810px;width:1200px;height:365px;background:var(--footer);color:var(--white)}
.foot-brand{position:absolute;left:98px;top:138px;display:flex;align-items:center;gap:12px}
.foot-brand .brand-mark{background:var(--white)}
.foot-brand .brand-name{color:var(--white)}
.foot-col{position:absolute;top:75px}
.foot-col h4{font-family:"Lato",Arial,sans-serif;font-weight:900;font-size:18px;text-transform:uppercase;margin-bottom:22px}
.foot-col li{list-style:none;font-size:13px;line-height:26px}
.foot-col p{font-size:13px;line-height:23px}
.email-field{width:254px;height:34px;background:var(--white);color:#777;font-size:13px;padding:8px 12px;margin-top:16px}
.sub-btn{margin-top:18px;width:100px;height:32px;background:var(--gold);border-radius:16px;font-family:"Lato",Arial,sans-serif;font-weight:700;font-size:12px;display:flex;align-items:center;justify-content:center}
.contact-row{display:flex;gap:20px;font-size:13px;line-height:22px;margin-bottom:20px}
.contact-row svg{flex:none;margin-top:3px}
.foot-rule{position:absolute;left:98px;top:290px;width:1004px;height:1px;background:#3a3a3a}
.copyright{position:absolute;left:98px;top:316px;font-size:12px}
.social{position:absolute;right:98px;top:308px;display:flex;gap:10px}
.social span{width:26px;height:26px;border-radius:50%;border:1.5px solid var(--white)}
</style>
</head>
<body>

<header class="site-header">
  <div class="brand"><span class="brand-mark"></span><span class="brand-name">Halvorn Minerals</span></div>
  <div class="topbar">
    <span><svg width="14" height="14" viewBox="0 0 24 24"><path fill="#b8913f" d="M6.6 10.8a15 15 0 0 0 6.6 6.6l2.2-2.2a1 1 0 0 1 1-.25 11.4 11.4 0 0 0 3.6.57 1 1 0 0 1 1 1V20a1 1 0 0 1-1 1A17 17 0 0 1 3 4a1 1 0 0 1 1-1h3.5a1 1 0 0 1 1 1c0 1.25.2 2.45.57 3.57a1 1 0 0 1-.25 1z"/></svg>1 555 014 2290</span>
    <span>|</span>
    <span><svg width="16" height="12" viewBox="0 0 16 12"><rect width="16" height="12" rx="1" fill="#b8913f"/><path d="M1 1l7 5 7-5" stroke="#fff" stroke-width="1.4" fill="none"/></svg>info@halvornminerals.com</span>
  </div>
  <nav class="main-nav">
    <span class="active">Home</span><span>Who we are</span><span>What we do</span><span>Corporate mission</span><span>Vision &amp; strategy</span><span>Contact us</span>
    <svg width="15" height="15" viewBox="0 0 16 16"><circle cx="6.5" cy="6.5" r="5" stroke="#1f1f1f" stroke-width="2" fill="none"/><path d="M10.5 10.5L15 15" stroke="#1f1f1f" stroke-width="2.2"/></svg>
  </nav>
</header>

<section class="hero" role="img" aria-label="City skyline at dusk with illuminated towers and highway interchange">
  <h2 class="hero-title">HALVORN MINERALS</h2>
  <p class="hero-sub">We are an international mining and private investment<br>company currently based in Dubai, UAE.</p>
  <div class="hero-btn">GET MORE INFO</div>
  <div class="dots"><span class="on"></span><span></span><span></span><span></span></div>
</section>

<section class="welcome-box">
  <h1 class="heading">Welcome to<br>Halvorn Minerals</h1>
  <p style="top:135px">Nemo enim ipsam voluptatem quia voluptas sit aspernatur aut oditaut fugit, sed quia consequuntur mag.</p>
  <p style="top:218px">Dolores eos qui ratione voluptatem sequi nesciunt. Neque porro quisam est, qui dolorem ipsum quia dolor sit amet, consectetur, adipisci velit,sed quia non numquam eius modi tempora.</p>
  <div class="btn" style="left:34px;top:325px;width:130px;height:44px">Read more</div>
</section>
<div class="video" role="img" aria-label="Video still of a bucket-wheel excavator at an open-pit mine">
  <svg width="60" height="60" viewBox="0 0 60 60"><circle cx="30" cy="30" r="28" fill="#111" stroke="#fff" stroke-width="3"/><path d="M24 18l18 12-18 12z" fill="#fff"/></svg>
</div>

<section class="services">
  <h2 class="heading section-title" style="top:68px">What we do</h2>
  <div class="service" style="left:97px">
    <svg width="142" height="142" viewBox="0 0 142 142"><circle cx="71" cy="71" r="69" fill="none" stroke="#1f1f1f" stroke-width="2"/><circle cx="71" cy="71" r="61" fill="#fff" stroke="#1f1f1f" stroke-width="6"/><rect x="56" y="58" width="28" height="28" rx="3" fill="none" stroke="#b8913f" stroke-width="3.5"/><path d="M66 77l3-8 15-15 5 5-15 15z" fill="#b8913f"/></svg>
    <h3>Global Mining</h3><p>Nam libero tempore, cum so luta nobis est eligendi optio cumq ue nihil impedit quo</p>
  </div>
  <div class="service" style="left:360px">
    <svg width="142" height="142" viewBox="0 0 142 142"><circle cx="71" cy="71" r="69" fill="none" stroke="#1f1f1f" stroke-width="2"/><circle cx="71" cy="71" r="61" fill="#fff" stroke="#1f1f1f" stroke-width="6"/><rect x="56" y="58" width="28" height="28" rx="3" fill="none" stroke="#b8913f" stroke-width="3.5"/><path d="M66 77l3-8 15-15 5 5-15 15z" fill="#b8913f"/></svg>
    <h3>Private Equity</h3><p>Nam libero tempore, cum so luta nobis est eligendi optio cumq ue nihil impedit quo</p>
  </div>
  <div class="service" style="left:623px">
    <svg width="142" height="142" viewBox="0 0 142 142"><circle cx="71" cy="71" r="69" fill="none" stroke="#1f1f1f" stroke-width="2"/><circle cx="71" cy="71" r="61" fill="#fff" stroke="#1f1f1f" stroke-width="6"/><rect x="56" y="58" width="28" height="28" rx="3" fill="none" stroke="#b8913f" stroke-width="3.5"/><path d="M66 77l3-8 15-15 5 5-15 15z" fill="#b8913f"/></svg>
    <h3>Professional Investor</h3><p>Nam libero tempore, cum so luta nobis est eligendi optio cumq ue nihil impedit quo</p>
  </div>
  <div class="service" style="left:885px">
    <svg width="142" height="142" viewBox="0 0 142 142"><circle cx="71" cy="71" r="69" fill="none" stroke="#1f1f1f" stroke-width="2"/><circle cx="71" cy="71" r="61" fill="#fff" stroke="#1f1f1f" stroke-width="6"/><rect x="56" y="58" width="28" height="28" rx="3" fill="none" stroke="#b8913f" stroke-width="3.5"/><path d="M66 77l3-8 15-15 5 5-15 15z" fill="#b8913f"/></svg>
    <h3>Asset Management</h3><p>Nam libero tempore, cum so luta nobis est eligendi optio cumq ue nihil impedit quo</p>
  </div>
</section>

<div class="why-photo" role="img" aria-label="Hand with a pen checking figures next to a calculator on a desk"></div>
<section class="why">
  <h2 class="heading">Why choose us?</h2>
  <ul>
    <li><svg width="14" height="14" viewBox="0 0 14 14"><circle cx="7" cy="7" r="7" fill="#b8913f"/><path d="M3.5 7l2.5 2.5 4.5-5" stroke="#fff" stroke-width="1.8" fill="none"/></svg>Nemo enim ipsam voluptatem quia voluptas sit aspernatur aiod it aut fugd quia consequuntur magni dol</li>
    <li><svg width="14" height="14" viewBox="0 0 14 14"><circle cx="7" cy="7" r="7" fill="#b8913f"/><path d="M3.5 7l2.5 2.5 4.5-5" stroke="#fff" stroke-width="1.8" fill="none"/></svg>Ut enim ad minima veniam, quis nostrum exercitationem ullam</li>
    <li><svg width="14" height="14" viewBox="0 0 14 14"><circle cx="7" cy="7" r="7" fill="#b8913f"/><path d="M3.5 7l2.5 2.5 4.5-5" stroke="#fff" stroke-width="1.8" fill="none"/></svg>Nemo enim ipsam voluptatem quia voluptas sit aspernatur aiod it aut fugd quia consequuntur magni dol</li>
    <li><svg width="14" height="14" viewBox="0 0 14 14"><circle cx="7" cy="7" r="7" fill="#b8913f"/><path d="M3.5 7l2.5 2.5 4.5-5" stroke="#fff" stroke-width="1.8" fill="none"/></svg>Ut enim ad minima veniam, quis nostrum exercitationem ullam it aut fugd quia consequuntur magni dol</li>
  </ul>
  <div class="btn" style="left:663px;top:2088px;width:130px;height:44px">Read more</div>
</section>

<section class="blog">
  <h2 class="heading section-title" style="top:2255px">Latest blog</h2>
  <article class="blog-card" style="left:98px">
    <div class="blog-img" role="img" aria-label="Drilling rig working inside an underground mine tunnel" style="background:linear-gradient(160deg,#2e2a26,#6b5d4c 55%,#a08c70)"></div>
    <h3>Finibus Bonorum et Malorum</h3>
    <div class="meta"><svg width="12" height="12" viewBox="0 0 12 12"><rect x="0.5" y="1.5" width="11" height="10" rx="1" fill="#b8913f"/></svg>25/09/2017<span class="sep">|</span><svg width="12" height="12" viewBox="0 0 12 12"><circle cx="6" cy="3.5" r="3" fill="#b8913f"/><path d="M0.5 12a5.5 5 0 0 1 11 0z" fill="#b8913f"/></svg>Elias</div>
    <p>Nemo enim ipsam voluptatem quia volupta asperna tur aut odit aut fugit, sed quia conseq.</p>
    <div class="read-more">Read more</div>
  </article>
  <article class="blog-card" style="left:438px">
    <div class="blog-img" role="img" aria-label="Hands holding a smartphone showing finance charts" style="background:linear-gradient(150deg,#cfe0ee,#5d8fbf 50%,#2f4f78)"></div>
    <h3>Finibus Bonorum et Malorum</h3>
    <div class="meta"><svg width="12" height="12" viewBox="0 0 12 12"><rect x="0.5" y="1.5" width="11" height="10" rx="1" fill="#b8913f"/></svg>25/09/2017<span class="sep">|</span><svg width="12" height="12" viewBox="0 0 12 12"><circle cx="6" cy="3.5" r="3" fill="#b8913f"/><path d="M0.5 12a5.5 5 0 0 1 11 0z" fill="#b8913f"/></svg>Elias</div>
    <p>Nemo enim ipsam voluptatem quia volupta asperna tur aut odit aut fugit, sed quia conseq.</p>
    <div class="read-more">Read more</div>
  </article>
  <article class="blog-card" style="left:778px">
    <div class="blog-img" role="img" aria-label="Terraced open-pit mine under a blue sky" style="background:linear-gradient(180deg,#6f9fd6 0%,#9fc0e2 28%,#c0623a 40%,#d9a070 70%,#a8553a)"></div>
    <h3>Finibus Bonorum et Malorum</h3>
    <div class="meta"><svg width="12" height="12" viewBox="0 0 12 12"><rect x="0.5" y="1.5" width="11" height="10" rx="1" fill="#b8913f"/></svg>25/09/2017<span class="sep">|</span><svg width="12" height="12" viewBox="0 0 12 12"><circle cx="6" cy="3.5" r="3" fill="#b8913f"/><path d="M0.5 12a5.5 5 0 0 1 11 0z" fill="#b8913f"/></svg>Elias</div>
    <p>Nemo enim ipsam voluptatem quia volupta asperna tur aut odit aut fugit, sed quia conseq.</p>
    <div class="read-more">Read more</div>
  </article>
</section>

<footer class="site-footer">
  <div class="foot-brand"><span class="brand-mark"></span><span class="brand-name">Halvorn Minerals</span></div>
  <div class="foot-col" style="left:438px">
    <h4>Information</h4>
    <ul><li>Home</li><li>who we are</li><li>What we do</li><li>Corporate mission</li><li>Vision &amp; strategy</li><li>Contact us</li></ul>
  </div>
  <div class="foot-col" style="left:610px">
    <h4>Newsletter subscription</h4>
    <p>Register your Email Address to get<br>information about us</p>
    <div class="email-field">Email Address</div>
    <div class="sub-btn">SUBSCRIBE</div>
  </div>
  <div class="foot-col" style="left:915px">
    <h4>Contact us</h4>
    <div class="contact-row"><svg width="12" height="16" viewBox="0 0 12 16"><path d="M6 0a6 6 0 0 1 6 6c0 4.5-6 10-6 10S0 10.5 0 6a6 6 0 0 1 6-6z" fill="#fff"/><circle cx="6" cy="6" r="2.2" fill="#161616"/></svg><span>Rua das Oliveiras, Lote 12<br>Lagoa - Portugal</span></div>
    <div class="contact-row"><svg width="14" height="14" viewBox="0 0 24 24"><path fill="#fff" d="M6.6 10.8a15 15 0 0 0 6.6 6.6l2.2-2.2a1 1 0 0 1 1-.25 11.4 11.4 0 0 0 3.6.57 1 1 0 0 1 1 1V20a1 1 0 0 1-1 1A17 17 0 0 1 3 4a1 1 0 0 1 1-1h3.5a1 1 0 0 1 1 1c0 1.25.2 2.45.57 3.57a1 1 0 0 1-.25 1z"/></svg><span>+1 555 014 2290</span></div>
    <div class="contact-row"><svg width="15" height="11" viewBox="0 0 16 12"><rect width="16" height="12" rx="1" fill="#fff"/><path d="M1 1l7 5 7-5" stroke="#161616" stroke-width="1.4" fill="none"/></svg><span>info@halvornminerals.com</span></div>
  </div>
  <div class="foot-rule"></div>
  <div class="copyright">Copyrights © 2018, Halvorn Minerals.  All rights reserved.</div>
  <div class="social"><span></span><span></span><span></span><span></span><span></span></div>
</footer>

</body>
</html>
```